Harlow Mailbox Services, full-service collaboration with postal service - installation of units

1. CBU - Cluster Box Unit - These are Mailbox units that you would see at residential neighborhoods, and Apartments -
2. Logo Needed
3. Maybe have CBU as a division of DWFS (Dermot Vance Field Services)
4. Card to be primary Harlow Mailbox Services

This is a letter of introduction that I am developing:

I am writing to introduce Dermot Vance Field Services, a company dedicated to delivering exceptional service and quality in the installation and maintenance of commercial mailboxes, specifically Cluster Box Units (CBUs). Our commitment to excellence and customer satisfaction has established us as a trusted partner for developers and postal services alike.
At Dermot Vance Field Services, we take pride in our comprehensive approach, ensuring that every step of the mailbox installation process is handled with precision and care. Our services include:
• Supplying high-quality CBUs tailored to meet the specific needs of your development.
• Providing a CBU plat layout upon approval of the address plat, ensuring seamless integration into your development plans.
• Collaborating with developers and postmasters to determine the optimal CBU locations for efficient mail delivery.
• Qualifying the labeling of CBU units, offering both sticker and etching options to suit your preferences.
• Pouring durable concrete foundations as required for the secure installation of the CBU units.
• Handling the installation process with expertise and attention to detail.
• Labeling the units and supplying keys for each mailbox, ensuring a smooth transition for residents and businesses.
Our team is dedicated to working closely with you to ensure that all requirements are met and that the installation process is completed efficiently and to the highest standards.
We look forward to the opportunity to collaborate with you and contribute to the success of your project. Please do not hesitate to contact us for any additional information or to discuss your specific requirements.
Sincerely,
Dermot Vance
Dermot Vance Field Services

Target Market(s)

Developers, Builders, Apartment's, HOA

Industry/Entity Type

Construction

Contact Information for Business Card

Name: Dermot Vance, Cell:555-671-0148, Email: derm@dvfieldco.example

Font styles to use
Serif

Requirements
Must have
• Fresh Looking
Nice to have
• Maybe a CBU Box if it looks clean
Should not have
• Not Industrial or Old traditional card

```html
<!DOCTYPE html>
<html lang="en">
<head>
<meta charset="utf-8">
<title>Harlow Mailbox Services — Business Card</title>
<link rel="stylesheet" href="https://fonts.googleapis.com/css2?family=Inter:wght@400;500;600&display=swap">
<style>
  :root {
    --page: #dcdde2;
    --card-light: #efefef;
    --band-grey: #a8a8a8;
    --rule-grey: #9a9a9a;
    --ink: #111111;
    --brand-blue: #0b4289;
    --white: #ffffff;
  }
  * { box-sizing: border-box; margin: 0; padding: 0; }
  html, body {
    width: 1200px; height: 900px; overflow: hidden;
    background: var(--page);
    font-family: "Inter", Arial, sans-serif;
  }
  .sheet {
    position: relative; width: 1200px; height: 900px;
    display: flex; flex-direction: column; align-items: center; justify-content: center; gap: 48px;
  }
  .card {
    position: relative; width: 640px; height: 366px; overflow: hidden;
  }

  /* Front */
  .card--front { background: var(--card-light); color: var(--ink); }
  .card__bands { position: absolute; inset: 0; }
  .brand {
    position: absolute; left: 70px; top: 88px;
    display: flex; align-items: center; gap: 14px;
  }
  .brand__square {
    width: 46px; height: 46px; border: 1.5px solid var(--brand-blue);
  }
  .brand__name { font-size: 30px; font-weight: 400; letter-spacing: 0.2px; white-space: nowrap; }
  .person { position: absolute; left: 70px; bottom: 80px; }
  .person__name { font-size: 36px; font-weight: 600; letter-spacing: -0.3px; line-height: 1; white-space: nowrap; }
  .person__title { font-size: 13px; margin-top: 8px; }
  .divider {
    position: absolute; left: 344px; top: 166px; width: 1.5px; height: 120px;
    background: var(--rule-grey);
  }
  .contacts {
    position: absolute; left: 364px; top: 160px;
    list-style: none; display: flex; flex-direction: column; gap: 12px;
  }
  .contact { display: flex; align-items: center; gap: 14px; font-size: 14px; white-space: nowrap; }
  .contact__icon {
    width: 32px; height: 32px; border-radius: 7px; background: var(--brand-blue);
    display: flex; align-items: center; justify-content: center; flex: none;
  }

  /* Back */
  .card--back {
    background: var(--brand-blue); color: var(--white);
    display: flex; align-items: center; justify-content: center;
  }
  .back-brand { display: flex; flex-direction: column; align-items: flex-start; gap: 12px; }
  .back-brand__row { display: flex; align-items: center; gap: 16px; }
  .back-brand__square { width: 58px; height: 58px; border: 1.5px solid var(--white); }
  .back-brand__name { font-size: 36px; font-weight: 400; letter-spacing: 0.3px; white-space: nowrap; }
  .back-brand__tagline { font-size: 12.5px; letter-spacing: 0.2px; padding-left: 74px; }
</style>
</head>
<body>
<main class="sheet">

  <section class="card card--front">
    <svg class="card__bands" width="640" height="366" viewBox="0 0 640 366" aria-hidden="true">
      <rect x="0" y="0" width="120" height="20" fill="var(--band-grey)"/>
      <rect x="130" y="0" width="250" height="20" fill="var(--band-grey)"/>
      <rect x="390" y="0" width="250" height="20" fill="var(--band-grey)"/>
      <rect x="0" y="346" width="250" height="20" fill="var(--band-grey)"/>
      <rect x="260" y="346" width="250" height="20" fill="var(--band-grey)"/>
      <rect x="520" y="346" width="120" height="20" fill="var(--band-grey)"/>
      <rect x="0" y="20" width="12" height="326" fill="var(--band-grey)"/>
      <rect x="628" y="20" width="12" height="326" fill="var(--band-grey)"/>
      <rect x="22" y="164" width="36" height="2" fill="var(--rule-grey)"/>
      <rect x="582" y="62" width="36" height="2" fill="var(--rule-grey)"/>
      <rect x="582" y="312" width="36" height="2" fill="var(--rule-grey)"/>
    </svg>

    <div class="brand">
      <span class="brand__square"></span>
      <span class="brand__name">Harlow Mailbox Services</span>
    </div>

    <div class="person">
      <p class="person__name">Dermot Vance</p>
      <p class="person__title">Founder &amp; Project Lead</p>
    </div>

    <span class="divider"></span>

    <ul class="contacts">
      <li class="contact">
        <span class="contact__icon">
          <svg width="16" height="16" viewBox="0 0 24 24" aria-hidden="true"><path fill="#fff" d="M6.6 10.8a15.1 15.1 0 0 0 6.6 6.6l2.2-2.2c.3-.3.7-.4 1-.2 1.1.4 2.3.6 3.6.6.6 0 1 .4 1 1V20c0 .6-.4 1-1 1A17 17 0 0 1 3 4c0-.6.4-1 1-1h3.5c.6 0 1 .4 1 1 0 1.3.2 2.5.6 3.6.1.3 0 .7-.2 1l-2.3 2.2z"/></svg>
        </span>
        <span>555-671-0148</span>
      </li>
      <li class="contact">
        <span class="contact__icon">
          <svg width="18" height="14" viewBox="0 0 18 14" aria-hidden="true"><rect x="1" y="1" width="16" height="12" fill="none" stroke="#fff" stroke-width="1.3"/><path d="M1 1l8 6.5L17 1" fill="none" stroke="#fff" stroke-width="1.3"/></svg>
        </span>
        <span>derm@dvfieldco.example</span>
      </li>
      <li class="contact">
        <span class="contact__icon">
          <svg width="18" height="18" viewBox="0 0 20 20" aria-hidden="true"><g fill="none" stroke="#fff" stroke-width="1.3"><circle cx="10" cy="10" r="8"/><ellipse cx="10" cy="10" rx="3.6" ry="8"/><path d="M2 10h16M3.2 6h13.6M3.2 14h13.6"/></g></svg>
        </span>
        <span>www.harlowmailbox.example</span>
      </li>
    </ul>
  </section>

  <section class="card card--back">
    <div class="back-brand">
      <div class="back-brand__row">
        <span class="back-brand__square"></span>
        <span class="back-brand__name">Harlow Mailbox Service</span>
      </div>
      <p class="back-brand__tagline">A Division of DWFS or Mailbox Solutions for Modern Living</p>
    </div>
  </section>

</main>
</body>
</html>
```